"KTR Community Supports" Business Card Design

We are a not for profit disability service that has recently changed its logo and trading name and is in the process of "rebranding".We provide employment, training and accommodation to people with disabilities. We find our new logo fresh and inspiring and would like our new business cards to reflect the same feeling. Our marketing line is "Learning, Belonging, Independence".

Target Market(s)

People with disabilities and their families, carers, support network

Industry/Entity Type

Business

Contact Information for Business Card

Requirements
Must have
• Our logo; space for the above listed information requirements

```html
<!DOCTYPE html>
<html lang="en">
<head>
<meta charset="utf-8">
<title>KTR Community Supports — Business Card</title>
<link rel="stylesheet" href="https://fonts.googleapis.com/css2?family=Open+Sans:wght@400;600;700&display=swap">
<style>
  :root {
    --canvas: #e9e6df;
    --white: #ffffff;
    --navy: #1d3f7a;
    --blue: #2b7fc1;
    --green-deep: #23521f;
    --green: #3f7d2c;
    --green-bright: #8cc63f;
    --leaf: #6aa535;
    --ink: #4a4a4a;
  }
  * { margin: 0; padding: 0; box-sizing: border-box; }
  html, body { width: 1200px; height: 1024px; overflow: hidden; }
  body {
    background: var(--canvas);
    font-family: "Open Sans", Arial, sans-serif;
    display: flex;
    flex-direction: column;
    align-items: center;
    justify-content: center;
    gap: 36px;
  }
  .card {
    position: relative;
    width: 800px;
    height: 457px;
    overflow: hidden;
    box-shadow: 0 6px 18px rgba(0,0,0,0.18);
  }
  /* Front */
  .card-front { background: var(--white); }
  .footer-strip {
    position: absolute;
    left: 0; right: 0; bottom: 0;
    height: 64px;
    background: linear-gradient(90deg, var(--green-deep) 0%, var(--green) 55%, var(--leaf) 100%);
    border-top: 4px solid var(--navy);
  }
  .brand {
    position: absolute;
    display: flex;
    align-items: center;
    gap: 12px;
    white-space: nowrap;
  }
  .brand-dot {
    flex: none;
    width: 24px; height: 24px; border-radius: 50%;
    background: var(--leaf);
  }
  .brand-name {
    font-weight: 700;
    font-size: 28px;
    color: var(--navy);
    letter-spacing: 0.5px;
  }
  .card-front .brand { left: 60px; top: 96px; }
  .contact-list {
    position: absolute;
    right: 60px; top: 62px;
    list-style: none;
    font-size: 15px;
    color: var(--ink);
    line-height: 27px;
  }
  .contact-list li { display: flex; align-items: center; gap: 10px; }
  .contact-list svg { width: 16px; height: 16px; fill: var(--navy); flex: none; }
  .person {
    position: absolute;
    left: 60px; top: 232px;
    color: var(--ink);
    font-size: 15px;
    line-height: 22px;
  }
  .person-name { color: var(--blue); font-weight: 700; font-size: 20px; letter-spacing: 0.5px; }
  .person-role { color: var(--leaf); font-weight: 600; font-size: 15px; margin-bottom: 4px; }
  .website {
    position: absolute;
    right: 40px; bottom: 20px;
    color: var(--white);
    font-size: 14px;
    letter-spacing: 0.3px;
  }
  /* Back */
  .card-back {
    background: radial-gradient(ellipse at 55% 45%, var(--green-bright) 0%, var(--green) 50%, var(--green-deep) 100%);
  }
  .card-back .brand {
    left: 50%; top: 46%;
    transform: translate(-50%, -50%);
  }
  .card-back .brand-dot { background: var(--white); }
  .card-back .brand-name { color: var(--white); }
  .tagline {
    position: absolute;
    left: 40px; bottom: 36px;
    color: var(--white);
    font-size: 16px;
    letter-spacing: 1.5px;
    text-transform: uppercase;
  }
</style>
</head>
<body>

<section class="card card-front" aria-label="Business card front">
  <div class="footer-strip" aria-hidden="true"></div>

  <div class="brand">
    <span class="brand-dot"></span>
    <span class="brand-name">KTR Community Supports</span>
  </div>

  <ul class="contact-list">
    <li><svg viewBox="0 0 16 16"><path d="M3 1h3l1.5 4-2 1.3a9 9 0 0 0 4.2 4.2L11 8.5l4 1.5v3a2 2 0 0 1-2 2A12 12 0 0 1 1 3a2 2 0 0 1 2-2z"/></svg>441 555 0142</li>
    <li><svg viewBox="0 0 16 16"><path d="M4 0h8a1 1 0 0 1 1 1v14a1 1 0 0 1-1 1H4a1 1 0 0 1-1-1V1a1 1 0 0 1 1-1zm1 2v10h6V2zm3 11a1 1 0 1 0 0 2 1 1 0 0 0 0-2z"/></svg>441 555 0187</li>
    <li><svg viewBox="0 0 16 16"><path d="M4 1h6v4H4zM2 6h12a1 1 0 0 1 1 1v6a1 1 0 0 1-1 1H2a1 1 0 0 1-1-1V7a1 1 0 0 1 1-1zm2 3v3h8V9z"/></svg>441 555 0163</li>
    <li><svg viewBox="0 0 16 16"><path d="M1 3h14v10H1zm1.5 1.2L8 8.5l5.5-4.3V4h-11z"/></svg>info@ktrsupports.org</li>
  </ul>

  <div class="person">
    <p class="person-name">MARCUS HALE</p>
    <p class="person-role">Managing Director</p>
    <p>Suite 204,</p>
    <p>17 Cedar Point Road</p>
    <p>Hamilton, HM05, Bermuda</p>
  </div>

  <p class="website">www.ktrsupports.org</p>
</section>

<section class="card card-back" aria-label="Business card back">
  <div class="brand">
    <span class="brand-dot"></span>
    <span class="brand-name">KTR Community Supports</span>
  </div>
  <p class="tagline">Learning, Belonging, Independence</p>
</section>

</body>
</html>
```